New Website for World Wide Charity (VELORA)

We need a dynamic web design for our brand new charity organisation that will be working worldwide. We will be funded by donations so need to attract people to donate.

What We Do
We work to optimise the wellbeing of the planet, the animals and all that live within. Our slogan is Achieving Vibrational Equilibrium.

We have included a Powerpoint document which may help you understand what we need, it is just an idea for structure and style, it is not set in stone so feel free to be as creative as you like!
Updates

Designs look the same

Target Market(s)

Adults 18+ with an interest in animal, environmental. Businesses that may like to support our natural world or already support our natural world.

Number of Pages Required

3 page

Colors

Designer to choose colors to be used in the design.

Requirements
Must have
• We need the website to be easy to use and understand.

Web pages will be Home, What We Do, Who We Are, Success Stories, What You Can Do (Blog section), Seek Help, Donate, Join.
Nice to have
• Natural feel, easy to navigate, Ideally the website will look natural and organic.

Natural colours, blues, greens, sand, gold, brown, grey, silver, Orange and yellow for impact.
Should not have
• Should not have a dark coloured theme.

```html
<!DOCTYPE html>
<html lang="en">
<head>
<meta charset="utf-8">
<title>VELORA — Help Raise World Vibration</title>
<link href="https://fonts.googleapis.com/css2?family=Montserrat:wght@700&family=Open+Sans:wght@400;600;700&display=swap" rel="stylesheet">
<style>
:root{
  --teal:#3b9aa6;
  --teal-soft:#4fb3bf;
  --green-rule:#4b8a5a;
  --ink:#111418;
  --body:#5b6168;
  --white:#ffffff;
  --footer:#0e0f10;
  --footer-line:#3a3c3f;
}
*{margin:0;padding:0;box-sizing:border-box}
html,body{width:1200px;height:2514px;overflow:hidden;background:var(--white)}
body{position:relative;font-family:'Open Sans',sans-serif;color:var(--ink)}
.abs{position:absolute}

.site-header{left:0;top:0;width:1200px;height:68px;background:var(--white);z-index:3}
.main-nav{right:113px;top:26px;display:flex;gap:24px;font-size:15px;color:var(--ink)}
.main-nav a{color:inherit;text-decoration:none;padding-bottom:8px}
.main-nav a.active{color:var(--teal);border-bottom:2px solid var(--teal)}
.brand-badge{left:94px;top:-2px;width:166px;height:166px;border-radius:50%;background:var(--white);z-index:4;display:flex;align-items:center;justify-content:center}
.brand-name{font-family:'Open Sans',sans-serif;font-weight:600;font-size:20px;letter-spacing:1px;color:#3d5a78}

.hero{left:0;top:68px;width:1200px;height:628px;
  background:radial-gradient(circle at 930px 360px,#6fbf4a 0,#3f8a32 120px,transparent 260px),
  radial-gradient(ellipse at 300px 120px,#d8d8a8 0,#8db66a 240px,transparent 520px),
  linear-gradient(180deg,#5d8f4d 0%,#4a8a38 55%,#2f5a22 85%,#1c3217 100%)}
.hero h1{left:110px;top:229px;font-family:'Montserrat',sans-serif;font-weight:700;font-size:31px;color:var(--white);letter-spacing:.3px}
.hero p{left:111px;top:280px;width:500px;font-size:17px;line-height:27px;color:var(--white);font-weight:600}
.btn{left:112px;top:361px;width:200px;height:43px;border-radius:22px;background:var(--teal);color:var(--white);font-weight:700;font-size:15px;display:flex;align-items:center;justify-content:center}

.cause-card{top:644px;width:311px;height:236px;display:flex;flex-direction:column;align-items:center;justify-content:center;z-index:2}
.cause-card h3{font-weight:400;font-size:21px;color:var(--white);letter-spacing:.3px}
.cause-card .more{margin-top:10px;font-weight:700;font-size:15px;color:var(--teal-soft);display:flex;align-items:center;gap:10px}
.card-env{left:111px;background:linear-gradient(160deg,#6c6a5a,#3d3f36 60%,#262824)}
.card-animal{left:445px;background:linear-gradient(180deg,#7c8a98 0%,#5b6570 45%,#6b5b45 75%,#7a6a54)}
.card-human{left:778px;background:linear-gradient(150deg,#4d5a3a,#36402a 55%,#2a2e22)}

.photo-frame{width:416px;height:307px;padding:4px;background:var(--white);box-shadow:0 0 6px rgba(0,0,0,.18)}
.photo-frame div{width:100%;height:100%}
.ph-env{background:linear-gradient(170deg,#9cbf72 0%,#7aa4c8 45%,#5a8e3c 100%)}
.ph-animal{background:linear-gradient(180deg,#8d8f9a 0%,#6e6a70 30%,#5a5e48 55%,#a07a40 80%,#8a6530)}
.ph-human{background:linear-gradient(170deg,#4a6a2e 0%,#7a9a52 45%,#5a5a4a 100%)}

.section-title{font-weight:600;font-size:31px;color:var(--ink);letter-spacing:.5px}
.rule{width:52px;height:2px;background:var(--green-rule)}
.copy{width:485px;font-size:15px;line-height:24px;color:var(--body);text-align:justify}
.copy p+p{margin-top:12px}

.site-footer{left:0;top:2182px;width:1200px;height:332px;background:var(--footer);color:var(--white)}
.footer-badge{left:114px;top:35px;width:140px;height:140px;border-radius:50%;border:3px solid #3d5a78;display:flex;align-items:center;justify-content:center}
.footer-badge .brand-name{color:#c9b6d8}
.social{top:218px;width:36px;height:36px;border-radius:50%;background:#222427}
.footer-col h4{font-weight:600;font-size:20px;margin-bottom:12px}
.footer-col li{list-style:none;font-size:15px;line-height:26px}
.contact-row{display:flex;gap:18px;font-size:15px;line-height:26px;margin-bottom:8px}
.contact-row svg{flex:none;margin-top:6px}
.footer-rule{left:111px;top:269px;width:978px;height:1px;background:var(--footer-line)}
.legal-line{top:286px;font-size:13px}
</style>
</head>
<body>

<header class="site-header abs">
  <nav class="main-nav abs">
    <a class="active">Home</a><a>What We Do</a><a>Who We Are</a><a>Success Stories</a><a>What You Can Do</a><a>Donate</a><a>Join</a>
  </nav>
</header>
<div class="brand-badge abs"><span class="brand-name">VELORA</span></div>

<section class="hero abs" role="img" aria-label="Cupped hands holding a glass globe above ferns and grass in a sunlit forest">
  <h1 class="abs">HELP RAISE WORLD VIBRATION</h1>
  <p class="abs">Lorem ipsum dolor sit amet, consectetur adipiscing elit sed do eiusmod tempor incididunt.</p>
  <div class="btn abs">MAKE A DIFFERENCE</div>
</section>

<div class="cause-card card-env abs" role="img" aria-label="Volunteers collecting litter in a forest">
  <h3>ENVIRONMENT</h3>
  <div class="more">FIND OUT MORE <svg width="13" height="13" viewBox="0 0 14 14"><circle cx="7" cy="7" r="6" fill="none" stroke="currentColor" stroke-width="1.6"/><path d="M4 7h5M7 4.5 9.5 7 7 9.5" fill="none" stroke="currentColor" stroke-width="1.6"/></svg></div>
</div>
<div class="cause-card card-animal abs" role="img" aria-label="Brown bear on a rocky mountain slope">
  <h3>ANIMAL</h3>
  <div class="more">FIND OUT MORE <svg width="13" height="13" viewBox="0 0 14 14"><circle cx="7" cy="7" r="6" fill="none" stroke="currentColor" stroke-width="1.6"/><path d="M4 7h5M7 4.5 9.5 7 7 9.5" fill="none" stroke="currentColor" stroke-width="1.6"/></svg></div>
</div>
<div class="cause-card card-human abs" role="img" aria-label="Child and grandparent picking fruit in an orchard">
  <h3>HUMAN</h3>
  <div class="more">FIND OUT MORE <svg width="13" height="13" viewBox="0 0 14 14"><circle cx="7" cy="7" r="6" fill="none" stroke="currentColor" stroke-width="1.6"/><path d="M4 7h5M7 4.5 9.5 7 7 9.5" fill="none" stroke="currentColor" stroke-width="1.6"/></svg></div>
</div>

<div class="photo-frame abs" style="left:111px;top:969px"><div class="ph-env" role="img" aria-label="Smiling volunteers planting and watering young plants"></div></div>
<h2 class="section-title abs" style="left:599px;top:984px">ENVIRONMENT</h2>
<div class="rule abs" style="left:600px;top:1029px"></div>
<div class="copy abs" style="left:601px;top:1052px">
  <p>Lorem ipsum dolor sit amet, consectetur adipiscing elit, sed do eiud tempor incididunt ut labore et dolore magna aliqua. Ut enim ad minim veniam, quis nostrud exercitation ullamco laboris nisi ut aliquip ex ea commodo consequat. Duis aute irure dolor in reprehenderit in voluptate velit esse cillum.</p>
  <p>Dolore eu fugiat nulla pariatur. Excepteur sint occaecat cupidatat non proident, sunt in culpa qui officia deserunt mollit anim id est laborumincididunt ut labore et dolore magna.</p>
</div>

<h2 class="section-title abs" style="left:109px;top:1388px">ANIMAL</h2>
<div class="rule abs" style="left:111px;top:1433px"></div>
<div class="copy abs" style="left:111px;top:1456px">
  <p>Lorem ipsum dolor sit amet, consectetur adipiscing elit, sed do eiud tempor incididunt ut labore et dolore magna aliqua. Ut enim ad minim veniam, quis nostrud exercitation ullamco laboris nisi ut aliquip ex ea commodo consequat. Duis aute irure dolor in reprehenderit in voluptate velit esse cillum.</p>
  <p>Dolore eu fugiat nulla pariatur. Excepteur sint occaecat cupidatat non proident, sunt in culpa qui officia deserunt mollit anim id est laborumincididunt ut labore et dolore magna.</p>
</div>
<div class="photo-frame abs" style="left:669px;top:1373px"><div class="ph-animal" role="img" aria-label="Red deer stag standing in golden grassland by a mountain lake"></div></div>

<div class="photo-frame abs" style="left:111px;top:1776px"><div class="ph-human" role="img" aria-label="Family walking along a wooden path through a forest"></div></div>
<h2 class="section-title abs" style="left:599px;top:1791px">HUMAN</h2>
<div class="rule abs" style="left:600px;top:1836px"></div>
<div class="copy abs" style="left:601px;top:1859px">
  <p>Lorem ipsum dolor sit amet, consectetur adipiscing elit, sed do eiud tempor incididunt ut labore et dolore magna aliqua. Ut enim ad minim veniam, quis nostrud exercitation ullamco laboris nisi ut aliquip ex ea commodo consequat. Duis aute irure dolor in reprehenderit in voluptate velit esse cillum.</p>
  <p>Dolore eu fugiat nulla pariatur. Excepteur sint occaecat cupidatat non proident, sunt in culpa qui officia deserunt mollit anim id est laborumincididunt ut labore et dolore magna.</p>
</div>

<footer class="site-footer abs">
  <div class="footer-badge abs"><span class="brand-name">VELORA</span></div>
  <span class="social abs" style="left:124px"></span>
  <span class="social abs" style="left:166px"></span>
  <span class="social abs" style="left:209px"></span>

  <div class="footer-col abs" style="left:378px;top:73px">
    <h4>Get Involved</h4>
    <ul><li>Join Us</li><li>Fundraise</li><li>Donate</li><li>Shop</li></ul>
  </div>
  <div class="footer-col abs" style="left:601px;top:73px">
    <h4>Contact Us</h4>
    <div class="contact-row"><svg width="12" height="14" viewBox="0 0 12 14"><path d="M6 0a5 5 0 0 0-5 5c0 3.5 5 9 5 9s5-5.5 5-9a5 5 0 0 0-5-5zm0 7a2 2 0 1 1 0-4 2 2 0 0 1 0 4z" fill="#6f8fc0"/></svg><span>Maya Linden, Willowbrook,<br>United States</span></div>
    <div class="contact-row"><svg width="14" height="14" viewBox="0 0 14 14"><path d="M3 1l2.5 3-1.5 1.5a8 8 0 0 0 4.5 4.5L10 8.5l3 2.5-1.5 2C6 13 1 8 1 2.5z" fill="#6f8fc0"/></svg><span>(555) 014 2290</span></div>
    <div class="contact-row"><svg width="15" height="12" viewBox="0 0 15 12"><rect x="0" y="1" width="15" height="10" rx="1" fill="#6f8fc0"/><path d="M0 2l7.5 5L15 2" fill="none" stroke="#0e0f10" stroke-width="1.2"/></svg><span>hello@velora.org</span></div>
  </div>
  <div class="footer-col abs" style="left:929px;top:73px">
    <h4>Legal</h4>
    <ul><li>Terms and Conditions</li><li>Cookies</li><li>Privacy Policy</li></ul>
  </div>

  <div class="footer-rule abs"></div>
  <div class="legal-line abs" style="left:111px">© Copyrights 2021 VELORA. All rights reserved</div>
  <div class="legal-line abs" style="left:939px;font-size:14px">Charity Number: <b>4172</b></div>
</footer>

</body>
</html>
```